Blast Off -

I need to launch a new website that more accurately reflects what we do as a business. We are an IT Reseller that specialises in delivering innovative solutions covering supply, implementation and support. My current website is www.norvexdtl.com and was something I designed myself on the Pin Rabbit website. This was fine for the first 2 years but now I need something more professional and detailed. A couple of websites for companies similar to Norvex DTL are www.bramwise.co.uk and www.quillbeck.co.uk. By looking at these it will hopefully give you an idea as to what I am trying to achieve.

Target Market(s)

UK based companies with between 30-250 employees, no fixed vertical

Coding

Coded - Design and coding required

Number of Pages Required

4 page

Font styles to use
Sans Serif

Colors
33a6d7
0592cd
85cae6

Requirements
Must have
• Contact details page to include a "Get in touch with us " section, About Us page, IT Support page to include the headings 1/ Proactive Monitoring 2/ 24 x 7 Support 3/ Security and Data Back-up 4/ Built-in Compliance (GDPR) 5/ Responsive IT Support. I am happy to provide the wording for these headings.
Clean crisp home screen with a Menu offering the requested drop down options.
Nice to have
• Easy to navigate site with a good flow. I have updated a page regarding cloud services, this would be great to have as a separate drop down menu option. I would like to have different Cloud logo's in ideally the Norvex Blue colour. Can you please add the photograph of Thornwick Hall which is my office in the contact us page.
Should not have
• I definitely DO NOT want a photo/view of London on the home page!!

```html
<!DOCTYPE html>
<html lang="en">
<head>
<meta charset="utf-8">
<title>Norvex DTL — IT Support</title>
<link href="https://fonts.googleapis.com/css2?family=Montserrat:ital,wght@0,400;0,500;0,600;0,700;1,400&display=swap" rel="stylesheet">
<style>
:root{
  --blue:#0592cd;
  --blue-mid:#33a6d7;
  --blue-light:#85cae6;
  --ink:#2b2b2b;
  --text:#3d3d3d;
  --muted:#6b6b6b;
  --line:#e4e8ec;
  --white:#ffffff;
  --hero-dark:#2e3a4a;
  --hero-mid:#4d5c70;
}
*{box-sizing:border-box;margin:0;padding:0}
html,body{width:1200px;height:2550px;overflow:hidden}
body{font-family:'Montserrat',sans-serif;color:var(--text);background:var(--white);position:relative}
.abs{position:absolute}
a{color:inherit;text-decoration:none}

/* header */
.site-header{position:absolute;left:0;top:0;width:1200px;height:62px;background:var(--white)}
.brand{position:absolute;left:225px;top:18px;display:flex;align-items:center;gap:8px;font-size:11px;font-weight:500;color:var(--ink)}
.brand-square{width:20px;height:20px;background:var(--blue);border-radius:3px}
.main-nav{position:absolute;left:411px;top:26px;display:flex;gap:22px;font-size:7.5px;font-weight:500;color:var(--ink);letter-spacing:.2px}
.header-phone{position:absolute;left:779px;top:26px;font-size:9px;font-weight:600;color:var(--blue);letter-spacing:.8px}
.header-cta{position:absolute;left:862px;top:18px;width:113px;height:25px;border-radius:13px;background:var(--blue);color:var(--white);font-size:7px;font-weight:700;display:flex;align-items:center;justify-content:center}

/* hero */
.hero{position:absolute;left:0;top:62px;width:1200px;height:374px;background:linear-gradient(110deg,#3b4657 0%,#52627a 45%,#3e4c60 70%,#6a7486 100%)}
.hero-title{position:absolute;left:223px;top:92px;font-size:23px;font-weight:600;color:var(--white)}
.hero-lead{position:absolute;left:225px;top:130px;width:480px;font-size:11.5px;line-height:17px;color:var(--white)}
.btn{display:flex;align-items:center;justify-content:center;font-size:11.5px;font-weight:500;border-radius:3px}
.btn-primary{background:var(--blue);color:var(--white)}
.btn-light{background:var(--white);color:var(--blue)}
.hero .btn{position:absolute;top:209px;width:141px;height:39px}
.features{position:absolute;left:765px;top:90px;list-style:none}
.features li{display:flex;align-items:center;gap:10px;height:37px;font-size:11px;font-weight:500;color:var(--white)}

/* trust card */
.card{position:absolute;background:var(--white);border-radius:8px;box-shadow:0 6px 24px rgba(20,40,70,.10)}
.trust{left:167px;top:383px;width:866px;height:197px}
.trust h2{position:absolute;width:100%;top:46px;text-align:center;font-size:22px;font-weight:500;color:var(--ink)}
.client-row{position:absolute;left:58px;top:120px;width:750px;display:flex;justify-content:space-between;align-items:center}
.client{display:flex;align-items:center;gap:6px;font-size:15px;font-weight:600;color:#2a2a2a}
.client i{display:block;width:10px;height:10px;background:var(--blue-light);border-radius:50%}
.chev{position:absolute}

/* section heading */
.section-mark{position:absolute;left:592px;width:16px;height:16px;background:var(--blue)}
.eyebrow{position:absolute;left:385px;font-size:12px;font-weight:500;color:var(--ink)}
.section-title{position:absolute;left:384px;font-size:23px;font-weight:500;color:var(--ink)}
.title-rule{position:absolute;left:385px;width:63px;height:3px;background:var(--blue)}

/* benefit cards */
.benefit{top:773px;width:231px;height:311px;border-radius:4px}
.benefit .art{position:absolute;left:60px;top:30px;width:110px;height:78px;border-radius:6px;background:linear-gradient(135deg,#d9ecf6,#9fd2ea)}
.benefit h3{position:absolute;left:18px;font-size:17px;font-weight:500;color:var(--ink)}
.benefit p{position:absolute;left:18px;width:200px;font-size:11px;line-height:17px;color:var(--text)}
.benefit .more{position:absolute;left:18px;top:273px;font-size:10.5px;font-weight:500;color:var(--blue)}

/* testimonial */
.quote-title{position:absolute;left:0;width:1200px;top:1272px;text-align:center;font-size:18px;font-weight:500;color:var(--blue)}
.quote-body{position:absolute;left:264px;top:1314px;width:680px;font-size:11px;line-height:28px;color:var(--ink)}
.client-name{position:absolute;left:0;width:1200px;text-align:center}
.dots{position:absolute;left:560px;top:1532px;display:flex;gap:9px}
.dots span{width:6px;height:6px;border-radius:50%;background:var(--blue-light)}
.dots span.on{background:var(--blue)}

/* steps */
.steps{left:167px;top:1601px;width:866px;height:281px;z-index:2}
.steps h2{position:absolute;width:100%;top:44px;text-align:center;font-size:23px;font-weight:500;color:var(--ink)}
.step{position:absolute;top:94px;display:flex;gap:10px}
.step b{font-size:20px;font-weight:500;color:var(--blue);line-height:22px}
.step p{font-size:11px;line-height:17px;color:var(--text);padding-top:2px}

/* contact band */
.contact-band{position:absolute;left:0;top:1822px;width:1200px;height:293px;background:linear-gradient(100deg,#1e86c0 0%,#2a9bd3 45%,#1b7fb8 100%)}
.contact-band .label{position:absolute;left:225px;top:166px;font-size:12px;font-weight:500;color:var(--white)}
.contact-band h2{position:absolute;left:225px;top:184px;font-size:22px;line-height:35px;font-weight:600;color:var(--white)}
.contact-band .rule{position:absolute;left:225px;top:260px;width:62px;height:3px;background:var(--white)}
.email-field{position:absolute;left:726px;top:148px;width:249px;height:38px;background:var(--white);border-radius:3px;font-size:12px;font-style:italic;color:var(--muted);padding:12px 18px}
.contact-band .btn{position:absolute;left:726px;top:200px;width:116px;height:38px}

/* footer */
.footer-brand{position:absolute;left:0;width:1200px;top:2178px;display:flex;justify-content:center;align-items:center;gap:12px;font-size:18px;font-weight:500;color:var(--ink)}
.footer-brand i{width:34px;height:34px;background:var(--blue);border-radius:4px}
.footer-col{position:absolute;top:2252px}
.footer-col h4{font-size:17px;font-weight:500;color:var(--ink);margin-bottom:10px}
.footer-col li{list-style:none;font-size:11px;color:var(--text);height:25px;line-height:25px}
.footer-col.contact li{height:28px;line-height:28px}
.divider{position:absolute;left:0;width:1200px;height:1px;background:var(--blue-light)}
.demo-line{position:absolute;left:225px;top:2456px;display:flex;align-items:center;gap:18px;font-size:16px;font-weight:500;color:var(--ink)}
.demo-line .btn{width:126px;height:34px;border-radius:17px;font-size:11px;font-weight:600}
.social{position:absolute;left:834px;top:2462px;display:flex;gap:17px}
.social span{width:22px;height:22px;border-radius:50%;background:var(--blue)}
.bottom-nav{position:absolute;left:224px;top:2518px;display:flex;gap:33px;font-size:11px;color:var(--text)}
.bottom-more{position:absolute;left:945px;top:2518px;font-size:11px;color:var(--text)}
</style>
</head>
<body>

<header class="site-header">
  <a class="brand"><span class="brand-square"></span>Norvex DTL</a>
  <nav class="main-nav"><a>ABOUT US</a><a>IT SUPPORT</a><a>CLOUD SERVICES</a><a>GET IN TOUCH</a></nav>
  <span class="header-phone">855 310-4827</span>
  <a class="header-cta">SOLVE YOUR IT ISSUES</a>
</header>

<section class="hero" role="img" aria-label="Photo of an IT team working at computers in an office">
  <h1 class="hero-title">Innovative Solutions For All IT Problems</h1>
  <p class="hero-lead">We are an IT Reseller that specialises in delivering innovative solutions covering supply, implementation and support.</p>
  <a class="btn btn-primary" style="left:225px">Get In Touch</a>
  <a class="btn btn-light" style="left:384px">Talk To Exerts</a>
  <ul class="features">
    <li><svg width="22" height="22" viewBox="0 0 22 22"><rect x="4" y="4" width="14" height="14" transform="rotate(45 11 11)" fill="#fff"/><path d="M7 11.5l3 3 5-6" stroke="#0592cd" stroke-width="2.2" fill="none"/></svg>RESPONSIVE IT SUPPORT</li>
    <li><svg width="22" height="22" viewBox="0 0 22 22"><rect x="4" y="4" width="14" height="14" transform="rotate(45 11 11)" fill="#fff"/><path d="M7 11.5l3 3 5-6" stroke="#0592cd" stroke-width="2.2" fill="none"/></svg>24/7 IT SUPPORT</li>
    <li><svg width="22" height="22" viewBox="0 0 22 22"><rect x="4" y="4" width="14" height="14" transform="rotate(45 11 11)" fill="#fff"/><path d="M7 11.5l3 3 5-6" stroke="#0592cd" stroke-width="2.2" fill="none"/></svg>SECURITY &amp; COMPLIANCE</li>
    <li><svg width="22" height="22" viewBox="0 0 22 22"><rect x="4" y="4" width="14" height="14" transform="rotate(45 11 11)" fill="#fff"/><path d="M7 11.5l3 3 5-6" stroke="#0592cd" stroke-width="2.2" fill="none"/></svg>BUILT-IN COMPLIANCE (GDPR)</li>
    <li><svg width="22" height="22" viewBox="0 0 22 22"><rect x="4" y="4" width="14" height="14" transform="rotate(45 11 11)" fill="#fff"/><path d="M7 11.5l3 3 5-6" stroke="#0592cd" stroke-width="2.2" fill="none"/></svg>SECURITY AND DATA BACK-UP</li>
  </ul>
</section>

<section class="card trust">
  <h2>Executives that trust Norvex DTL</h2>
  <svg class="chev" style="left:22px;top:128px" width="12" height="18" viewBox="0 0 12 18"><path d="M9 2L3 9l6 7" stroke="#222" stroke-width="2.2" fill="none"/></svg>
  <div class="client-row">
    <span class="client">Brixella</span>
    <span class="client"><i></i>Voltarn</span>
    <span class="client">Hendrow</span>
    <span class="client">Kestrel Fuels</span>
    <span class="client"><i></i>Tallowmere</span>
    <span class="client">Foundry Post</span>
  </div>
  <svg class="chev" style="left:834px;top:128px" width="12" height="18" viewBox="0 0 12 18"><path d="M3 2l6 7-6 7" stroke="#222" stroke-width="2.2" fill="none"/></svg>
</section>

<section class="why">
  <span class="section-mark" style="top:650px"></span>
  <span class="eyebrow" style="top:690px">Why Us ?</span>
  <h2 class="section-title" style="top:704px">How we save you from all the trouble</h2>
  <span class="title-rule" style="top:739px"></span>
  <svg class="chev" style="left:183px;top:864px" width="12" height="18" viewBox="0 0 12 18"><path d="M9 2L3 9l6 7" stroke="#222" stroke-width="2.2" fill="none"/></svg>
  <article class="card benefit" style="left:225px">
    <div class="art" role="img" aria-label="Illustration of a person beside a speed gauge"></div>
    <h3 style="top:120px">Ultra-Fast Response</h3>
    <p style="top:160px">Talk to a qualified engineer straight away. Your IT issues don't spend hours sitting in a queue.</p>
    <a class="more">Learn More</a>
  </article>
  <article class="card benefit" style="left:484px">
    <div class="art" role="img" aria-label="Illustration of a person presenting a rising line chart"></div>
    <h3 style="top:122px">Increased Productivity</h3>
    <p style="top:162px">We understand that you shouldn't have to be a technology expert to run a business. Spend your time on your business and not fixing your technology.</p>
    <a class="more">Learn More</a>
  </article>
  <article class="card benefit" style="left:744px">
    <div class="art" role="img" aria-label="Illustration of a person beside a large clock"></div>
    <h3 style="top:117px">Minimal Downtime</h3>
    <p style="top:156px">Your business can't make money if your IT keeps going down. You deserve an IT company that cares about your business as much as you do.</p>
    <a class="more">Learn More</a>
  </article>
  <svg class="chev" style="left:1004px;top:864px" width="12" height="18" viewBox="0 0 12 18"><path d="M3 2l6 7-6 7" stroke="#222" stroke-width="2.2" fill="none"/></svg>
</section>

<section class="stories">
  <span class="section-mark" style="top:1153px"></span>
  <span class="eyebrow" style="top:1195px">Success Stories</span>
  <h2 class="section-title" style="top:1208px">Work with us and get results like this</h2>
  <span class="title-rule" style="top:1243px"></span>
  <p class="quote-title">“Came up with excellent solutions and...”</p>
  <svg class="chev" style="left:223px;top:1350px" width="12" height="18" viewBox="0 0 12 18"><path d="M9 2L3 9l6 7" stroke="#222" stroke-width="2.2" fill="none"/></svg>
  <p class="quote-body">“Prior to working with Tellwright, our staff were regularly experiencing a range of really frustrating IT problems. Norvex DTL came up with excellent solutions and have maintained our systems ever since. Engineers are always available and easy to contact. I thoroughly recommend them”</p>
  <svg class="chev" style="left:965px;top:1350px" width="12" height="18" viewBox="0 0 12 18"><path d="M3 2l6 7-6 7" stroke="#222" stroke-width="2.2" fill="none"/></svg>
  <p class="client-name" style="top:1428px;font-size:28px;font-weight:500;color:#1f3f9a">QIG</p>
  <p class="client-name" style="top:1470px;font-size:12px;font-weight:600;color:var(--ink)">Quorvane Insight Group</p>
  <p class="client-name" style="top:1486px;font-size:11px;font-style:italic;color:var(--text)">Market research company</p>
  <div class="dots"><span></span><span class="on"></span><span></span><span></span><span></span><span></span></div>
</section>

<section class="card steps">
  <h2>Take first step to get the IT support your business deserves</h2>
  <div class="step" style="left:58px;width:225px"><b>1.</b><p>Get in touch. We would love to hear about your business and the IT issues you are currently facing.</p></div>
  <div class="step" style="left:320px;width:235px"><b>2.</b><p>Tell us about your business and how you use IT. By understanding your business we can create the right support for you.</p></div>
  <div class="step" style="left:590px;width:225px"><b>3.</b><p>Say goodbye to IT headaches and time spent trying to get your technology to work.</p></div>
  <a class="btn btn-primary" style="position:absolute;left:363px;top:193px;width:140px;height:38px">Get Started</a>
</section>

<section class="contact-band" role="img" aria-label="Blue-toned photo of a team meeting in an open office">
  <span class="section-mark" style="left:225px;top:132px;background:#fff"></span>
  <span class="label">Talk To Us</span>
  <h2>Want to learn more?<br>Need some help with IT services?</h2>
  <span class="rule"></span>
  <div class="email-field">Email</div>
  <a class="btn btn-light">Talk To Us</a>
</section>

<footer>
  <div class="footer-brand"><i></i>Norvex DTL</div>
  <div class="footer-col" style="left:224px"><h4>Services</h4><ul><li>Cloud Services</li><li>IT Services</li><li>Connectivity</li><li>IT Security</li><li>Backup</li></ul></div>
  <div class="footer-col" style="left:424px;top:2249px"><h4>About us</h4><ul><li>Team</li><li>News</li><li>Blog</li><li>Partners</li><li>Careers</li></ul></div>
  <div class="footer-col" style="left:629px;top:2249px"><h4>Legal</h4><ul><li>Privacy Policy</li><li>Terms of Use</li></ul></div>
  <div class="footer-col contact" style="left:804px;top:2249px"><h4>Get in touch</h4><ul><li style="height:38px">01632 960 418</li><li>Thornwick Hall, Elm Colney,</li><li>Westford, Hartshire,</li><li>WF2 4QT, United Kingdom</li></ul></div>
  <span class="divider" style="top:2441px"></span>
  <div class="demo-line">Want to try our services ?<a class="btn btn-primary">Request a Demo</a></div>
  <div class="social"><span></span><span></span><span></span><span></span></div>
  <span class="divider" style="top:2506px"></span>
  <nav class="bottom-nav"><a>IT Support</a><a>Get In Touch</a><a>Cloud Services</a><a>About Us</a></nav>
  <a class="bottom-more">More</a>
</footer>

</body>
</html>
```